TGCo Wholesale Flyer

I need a wholesaler flyer/letter put together. I've provided copy and a range of photos for the designer to use. The flyer needs to match the same colour pallet and style of tallowmeregoodsco.com.au.

It will be used to send to new potenial retailers so needs to look smick.

```html
<!DOCTYPE html>
<html lang="en">
<head>
<meta charset="utf-8">
<title>TGCo Wholesale Flyer</title>
<link href="https://fonts.googleapis.com/css2?family=Cormorant+Garamond:wght@500&family=Libre+Baskerville:wght@400;700&family=Figtree:wght@400;700&family=Roboto+Condensed:wght@700&display=swap" rel="stylesheet">
<style>
:root{
  --backdrop:#6e6d5f;
  --paper:#efeee6;
  --band:#c9c3ad;
  --ink:#1d1c18;
  --maroon:#5a1c10;
  --olive:#4c4a16;
  --olive-soft:#5d5b22;
  --foot:#8f9880;
  --mono:#a9a9a6;
}
*{box-sizing:border-box;margin:0;padding:0}
html,body{width:969px;height:1200px;overflow:hidden;background:var(--backdrop)}
.flyer{position:absolute;left:135px;top:107px;width:698px;height:986px;background:var(--paper);color:var(--ink);font-family:"Figtree",sans-serif}
.monogram{position:absolute;left:34px;top:40px;font-family:"Cormorant Garamond",serif;font-weight:500;font-size:34px;color:var(--mono);letter-spacing:-1px}
.wordmark{position:absolute;left:259px;top:26px;width:200px;text-align:center;font-family:"Cormorant Garamond",serif;font-weight:500;font-size:28px;line-height:23px;letter-spacing:.5px}
.values{position:absolute;left:0;top:119px;width:698px;height:68px;background:var(--band)}
.value{position:absolute;top:14px;text-align:center;font-family:"Libre Baskerville",serif;font-weight:700;font-size:14.5px;line-height:21px;color:var(--ink);white-space:nowrap}
.value-icon{position:absolute}
.map-icon{left:22px;top:13px;width:47px;height:42px;background:#b7b09a;border-radius:6px}
.photo{position:absolute}
.photo-products{left:26px;top:207px;width:319px;height:241px;background:linear-gradient(160deg,#9aa98a 0%,#6f7a5e 45%,#5a4530 75%,#2c2620 100%)}
.photo-soap{left:27px;top:465px;width:185px;height:187px;background:linear-gradient(135deg,#4f4a42 0%,#7a6f5e 45%,#d8cfa8 60%,#3d3a33 100%)}
.photo-cattle{left:28px;top:670px;width:183px;height:134px;background:radial-gradient(ellipse at 45% 55%,#a8652a 0%,#8b6a35 35%,#7e8a3c 70%,#6f7a36 100%)}
.photo-basket{left:228px;top:465px;width:116px;height:339px;background:linear-gradient(180deg,#d9cfc2 0%,#b89a72 40%,#7d6440 75%,#5c4a2e 100%)}
.photo-diffuser{left:571px;top:649px;width:127px;height:179px;background:linear-gradient(180deg,rgba(239,238,230,0) 0%,#e9e3d6 55%,#c9b394 85%,#e6dccb 100%)}
.intro{position:absolute;left:374px;top:206px;width:283px;font-size:12.3px;line-height:16.8px;text-align:justify}
.section-title{position:absolute;left:374px;font-family:"Libre Baskerville",serif;font-size:15.3px;letter-spacing:.2px}
.partner-title{top:362px;color:var(--maroon)}
.range-title{top:685px;color:var(--olive-soft)}
.reasons{position:absolute;left:374px;top:408px;width:290px;list-style:none}
.reason{height:60px}
.reason h3{font-family:"Roboto Condensed",sans-serif;font-weight:700;font-size:12.6px;line-height:16.8px;color:var(--maroon)}
.reason p{font-size:12.3px;line-height:16.8px}
.range{position:absolute;left:376px;top:721px;list-style:none;font-weight:700;font-size:12.4px;color:var(--olive);line-height:16.8px}
.range li{margin-bottom:6.6px}
.cta{position:absolute;left:215px;top:824px;width:267px;height:30px;background:var(--olive);color:var(--paper);font-family:"Libre Baskerville",serif;font-size:18px;line-height:30px;text-align:center;letter-spacing:.2px}
.contact-lead{position:absolute;left:0;top:869px;width:690px;text-align:center;font-weight:700;font-size:14.4px;color:var(--olive)}
.contact{position:absolute;display:flex;align-items:center;gap:8px;font-weight:700;font-size:12.6px;color:var(--olive)}
.contact svg{flex:none}
.dot{width:21px;height:21px;border:2px solid var(--olive);border-radius:50%}
.foot-bar{position:absolute;left:0;bottom:0;width:698px;height:15px;background:var(--foot)}
</style>
</head>
<body>
<main class="flyer">
  <div class="monogram">TGCo</div>
  <h1 class="wordmark">TALLOWMERE GOODS CO.</h1>

  <section class="values">
    <div class="value-icon map-icon" role="img" aria-label="Outline map of Australia"></div>
    <div class="value" style="left:78px;width:166px">AUSTRALIAN<br>OWNED &amp; OPERATED</div>

    <svg class="value-icon" style="left:287px;top:14px" width="28" height="36" viewBox="0 0 28 36" fill="none" stroke="#1d1c18" stroke-width="1.4">
      <path d="M4 34 C6 20 12 8 26 2 C26 16 18 28 6 30"/><path d="M4 34 L17 14"/>
    </svg>
    <div class="value" style="left:322px;width:124px">ECO-FRIENDLY<br>&amp; REFILLABLE</div>

    <svg class="value-icon" style="left:511px;top:20px" width="30" height="30" viewBox="0 0 30 30" fill="none" stroke="#1d1c18" stroke-width="1.8">
      <path d="M3 3 C8 12 14 20 28 27"/><path d="M10 14 C6 18 8 24 14 24"/><path d="M16 19 C15 12 19 8 24 7 C25 14 21 19 16 19"/><path d="M6 8 C3 12 4 16 8 17"/>
    </svg>
    <div class="value" style="left:540px;width:124px">HANDCRAFTED<br>IN TASMANIA</div>
  </section>

  <div class="photo photo-products" role="img" aria-label="Candle jar, room mist bottle and small jar on a wooden table with succulents"></div>
  <div class="photo photo-soap" role="img" aria-label="Bars of handmade soap on a rustic wooden crate with fresh herbs"></div>
  <div class="photo photo-cattle" role="img" aria-label="Highland cattle standing in a green paddock"></div>
  <div class="photo photo-basket" role="img" aria-label="Hands holding a woven basket with refill pouches and wildflowers"></div>

  <p class="intro">Handcrafted in small batches on our Tasmanian farm since 2014, Tallowmere Goods Co. offers an honest and meaningful range of natural soy candles, diffusers, and body care. We use self-grown or locally sourced botanicals and are committed to simple methods, minimising plastic, and remaining cruelty-free.</p>

  <h2 class="section-title partner-title">WHY PARTNER WITH US?</h2>
  <ul class="reasons">
    <li class="reason"><h3>Authentic Tasmanian Origin:</h3><p>Handcrafted on our family's Fernhollow Farm<br>since 2014.</p></li>
    <li class="reason"><h3>Natural Ingredients:</h3><p>Made with botanicals grown on our farm or<br>sourced locally.</p></li>
    <li class="reason"><h3>Artisanal Quality:</h3><p>Candles, diffusers, and body products made<br>in small, carefully blended batches.</p></li>
    <li class="reason"><h3>Ethically Produced:</h3><p>Committed to minimising single-use<br>plastics and proudly cruelty-free.</p></li>
  </ul>

  <h2 class="section-title range-title">OUR PRODUCT RANGE</h2>
  <ul class="range">
    <li>Natural Soy Candles</li>
    <li>Diffusers &amp; Room Mists</li>
    <li>Artisanal Soaps &amp;<br>Body Products</li>
  </ul>
  <div class="photo photo-diffuser" role="img" aria-label="Reed diffuser on a round wooden tray with dried flowers"></div>

  <div class="cta">JOIN OUR RETAIL FAMILY</div>
  <p class="contact-lead">For wholesale inquiries or to request our full catalog, please contact us:</p>

  <div class="contact" style="left:66px;top:900px"><span class="dot"></span>tallowmeregoods.co</div>
  <div class="contact" style="left:66px;top:928px">
    <svg width="26" height="26" viewBox="0 0 26 26" fill="none" stroke="#4c4a16" stroke-width="1.8"><circle cx="13" cy="13" r="11.5"/><path d="M8.5 7.5 L10.5 7 L12 10 L10.6 11.3 C11.4 13 12.8 14.5 14.6 15.4 L15.9 14 L19 15.5 L18.5 17.6 C13 18.5 7.5 13 8.5 7.5 Z" fill="#4c4a16"/></svg>
    0412 345 678
  </div>
  <div class="contact" style="left:384px;top:901px">
    <svg width="22" height="18" viewBox="0 0 22 18" fill="none" stroke="#4c4a16" stroke-width="1.5"><rect x="1" y="2" width="20" height="14"/><path d="M1 2 L11 10 L21 2"/></svg>
    hello@tallowmeregoodsco.com.au
  </div>
  <div class="contact" style="left:384px;top:929px">
    <svg width="23" height="23" viewBox="0 0 24 24" fill="none" stroke="#4c4a16" stroke-width="1.3"><circle cx="12" cy="12" r="10.5"/><ellipse cx="12" cy="12" rx="4.5" ry="10.5"/><path d="M1.5 12 H22.5 M3.5 6.5 H20.5 M3.5 17.5 H20.5 M12 1.5 V22.5"/></svg>
    www.tallowmeregoodsco.com.au
  </div>

  <div class="foot-bar"></div>
</main>
</body>
</html>
```